Verdantor Business Card Design

We need a modern, clean, business card design for our hardscape solution company. I have outlined our specialist areas in the card information section. We meet and greet and wish to build relationships with large-scale builders and project managers of large-scale building companies. Hence the reason for the business card.We want them to understand we are their 'solution' and we will make their working life easier and less stressful. We also are the highest quality construction with an exceptional eye for detail taking a lot of pressure off the project managers. I have done a few mock-ups myself but would like to see what else can be created. We are open to black or white (or grey) background.

Industry/Entity Type

Construction

Contact Information for Business Card

Dean Carrow - Director
0471 583 902
dean@verdantorgroup.com

www.verdantorgroup.com.au

"Hardscape Construction Solutions for Large-Scale Builders" (front)

Logo already designed and to be added.

REAR:

Your One-Stop Hardscape Solution For:

Retirement Village & Community Development Construction

- Synthetic Sports Fields - Bowling Greens
- Tennis Courts - Concreting
- Paving - Landscape

www.verdantorgroup.com

```html
<!DOCTYPE html>
<html lang="en">
<head>
<meta charset="utf-8">
<title>Verdantor Business Card</title>
<link rel="stylesheet" href="https://fonts.googleapis.com/css2?family=PT+Sans:wght@400;700&family=PT+Sans+Narrow:wght@700&display=swap">
<style>
  :root {
    --backdrop: #6a6a6a;
    --card: #3a3a3a;
    --scene-tone: #474747;
    --green: #a6c83a;
    --blue: #1ba5e2;
  }
  * { margin: 0; padding: 0; box-sizing: border-box; }
  html, body {
    width: 1000px; height: 1200px; overflow: hidden;
    background: var(--backdrop);
    font-family: "PT Sans", sans-serif;
  }
  .canvas { position: relative; width: 1000px; height: 1200px; }
  .card {
    position: absolute; left: 112px; width: 776px; height: 478px;
    background: var(--card); overflow: hidden;
  }
  .card--front { top: 82px; }
  .card--back { top: 645px; }
  .scene { position: absolute; opacity: 0.55; }
  .card--front .scene {
    left: 0; top: 110px; width: 640px; height: 330px;
    background: radial-gradient(ellipse at 55% 55%, var(--scene-tone) 0%, rgba(71,71,71,0) 70%);
  }
  .card--back .scene {
    left: 200px; top: 60px; width: 576px; height: 300px;
    background: radial-gradient(ellipse at 60% 50%, var(--scene-tone) 0%, rgba(71,71,71,0) 70%);
  }
  .brand-name {
    position: absolute; left: 30px; top: 62px;
    font-weight: 700; font-size: 82px; line-height: 1;
    color: var(--green); letter-spacing: -1px;
  }
  .contact {
    position: absolute; right: 30px; top: 200px; text-align: right;
    font-size: 22px; line-height: 31.5px; color: var(--green);
  }
  .contact__name { color: var(--blue); font-weight: 700; }
  .contact__role { font-weight: 700; font-size: 23px; letter-spacing: 6px; margin-right: -6px; }
  .contact__line { font-weight: 700; letter-spacing: 1.5px; margin-right: -1.5px; }
  .tagline {
    position: absolute; right: 30px; top: 390px; text-align: right;
    font-size: 21px; line-height: 31px; color: var(--blue);
  }
  .tagline__wide { letter-spacing: 3.9px; margin-right: -3.9px; }
  .services-heading {
    position: absolute; left: 33px; top: 28px;
    font-weight: 700; font-size: 21px; line-height: 32px; color: var(--blue);
  }
  .services-heading__wide { letter-spacing: 13.5px; }
  .services-heading__tight { letter-spacing: 3px; }
  .services-list {
    position: absolute; left: 33px; top: 134px; width: 325px;
    font-family: "PT Sans Narrow", sans-serif; font-weight: 700;
    font-size: 24px; line-height: 26px; letter-spacing: -1px;
    color: var(--green);
  }
  .back-url {
    position: absolute; right: 30px; bottom: 30px;
    font-family: "PT Sans Narrow", sans-serif; font-weight: 700;
    font-size: 25px; letter-spacing: 0.6px; color: var(--green);
  }
</style>
</head>
<body>
<div class="canvas">
  <section class="card card--front">
    <div class="scene" role="img" aria-label="Faint background image of a construction site"></div>
    <div class="brand-name">Verdantor</div>
    <div class="contact">
      <div class="contact__name">DEAN CARROW</div>
      <div class="contact__role">Director</div>
      <div class="contact__line">0471 583 902</div>
      <div class="contact__line">dean@verdantorgroup.com</div>
      <div class="contact__line">www.verdantorgroup.com.au</div>
    </div>
    <div class="tagline">
      <div>Hardscape Construction Solutions</div>
      <div class="tagline__wide">for Large-Scale Builders</div>
    </div>
  </section>

  <section class="card card--back">
    <div class="scene" role="img" aria-label="Faint background image of buildings under construction"></div>
    <h2 class="services-heading">
      <div class="services-heading__wide">YOUR ONE-STOP</div>
      <div class="services-heading__tight">HARDSCAPE SOLUTION FOR</div>
    </h2>
    <p class="services-list">Retirement Village &amp; Community Development Construction » Synthetic Sports Fields » Bowling Greens » Tennis Courts » Concreting » Paving » Landscape</p>
    <div class="back-url">WWW.VERDANTORGROUP.COM.AU</div>
  </section>
</div>
</body>
</html>
```